Design needed for Cover of Conference Brochure

We are a conference company that puts on several business conferences per year. We are putting together a new conference - the Clearpath Forum Week, and our audience is UX practitioners and specialists, product designers, UX designers, etc.
We need a brochure cover created. We are looking for fresh design ideas and are open to varying color schemes - please just keep in mind that this is a conference for business professionals, and fonts and colors should reflect this. Only restriction is that we do have a general cover format that we follow - i.e. which text goes where. (I've attached samples from our other events to reference.) We also generally have a central image to each brochure - feel free to submit a few versions with different images... we want something that accurately represents UX. However, if the design is compelling enough, image might not be completely necessary. We are relatively flexible - we just want something sharp!
- Must include BWKT logo (see placing on sample event covers)
- Must include footer - see sample covers
- Red text in word document are notes to you the designer - not actual text meant to appear on the cover
This cover is standard 8x11, and will be used for web only, not print. I have attached a word doc that includes all of the text that you will need for the cover. We will need final version in PDF, jpeg, and PSD. Please message me with any questions or clarification.

```html
<!DOCTYPE html>
<html lang="en">
<head>
<meta charset="utf-8">
<title>Clearpath Forum Week – Brochure Cover</title>
<link rel="stylesheet" href="https://fonts.googleapis.com/css2?family=Oswald:wght@500;600;700&family=Arimo:wght@400;700&display=swap">
<style>
  :root{
    --navy:#0b2859;
    --navy-deep:#071d44;
    --sky:#29a8ec;
    --ribbon:#4c7fe0;
    --ink:#0d2a5c;
    --white:#ffffff;
    --orange:#ff8a00;
    --red:#d6121b;
    --peach:rgba(240,200,160,.62);
    --blue-soft:rgba(150,200,235,.62);
    --green-soft:rgba(205,235,150,.62);
    --pink-soft:rgba(235,180,235,.62);
  }
  *{margin:0;padding:0;box-sizing:border-box}
  html,body{width:873px;height:1200px;overflow:hidden;background:#fff}
  .cover{position:relative;width:873px;height:1200px;overflow:hidden;font-family:"Arimo",Arial,sans-serif;color:var(--ink)}

  .hero-photo{position:absolute;left:0;top:323px;width:873px;height:877px;
    background:linear-gradient(90deg,#e7edf2 0%,#dfe6ec 35%,#c9c2bf 60%,#d5dbe2 85%,#e4eaef 100%)}
  .hero-photo::after{content:"";position:absolute;left:0;right:0;bottom:0;height:110px;background:linear-gradient(#f3f5f7,#ffffff)}

  .header{position:absolute;left:0;top:0;width:873px;height:261px;
    background:linear-gradient(180deg,#0e2f66 0%,var(--navy) 55%,var(--navy-deep) 100%)}
  .date-ribbon{position:absolute;left:553px;top:18px;width:320px;height:76px}
  .date-ribbon span{position:absolute;left:54px;top:20px;font:400 30px/1.2 "Arimo",sans-serif;color:var(--ink);white-space:nowrap}

  .brand{position:absolute;left:21px;top:80px;width:144px;height:144px;border-radius:18px;
    background:linear-gradient(180deg,#5fc4f7,#1d8fd8);border:4px solid #d7eefc;
    display:flex;align-items:center;justify-content:center}
  .brand span{font:700 38px "Oswald",sans-serif;color:var(--white);letter-spacing:1px}

  .title{position:absolute;left:182px;top:96px;width:670px;font-family:"Oswald",sans-serif;font-weight:700;line-height:1;white-space:nowrap;letter-spacing:.5px}
  .title .lead{color:var(--white);font-size:74px}
  .title .rest{color:var(--sky);font-size:62px}
  .tagline{position:absolute;left:184px;top:183px;font:500 26px "Oswald",sans-serif;color:var(--white);letter-spacing:.2px;white-space:nowrap}

  .venue-bar{position:absolute;left:0;top:261px;width:873px;height:62px;
    background:linear-gradient(180deg,#36b3f1,#1c95dd);border-top:3px solid #0a2a5e;border-bottom:3px solid #0a2a5e}
  .venue-bar svg{position:absolute;left:26px;top:14px}
  .venue-bar p{position:absolute;left:118px;top:10px;font:400 33px "Arimo",sans-serif;color:var(--white);white-space:nowrap}

  .bubble{position:absolute;border-radius:50%;display:flex;flex-direction:column;align-items:center;justify-content:center;text-align:center}
  .bubble h3{font:700 31px/1.1 "Arimo",sans-serif;color:var(--ink)}
  .bubble p{font:400 22px/1.3 "Arimo",sans-serif;color:var(--ink)}
  .bubble-learn{left:-23px;top:303px;width:274px;height:274px;background:var(--peach)}
  .bubble-cases{left:174px;top:462px;width:274px;height:274px;background:var(--blue-soft)}
  .bubble-team{left:-8px;top:553px;width:244px;height:244px;background:var(--green-soft)}
  .bubble-insights{left:136px;top:712px;width:288px;height:288px;background:var(--pink-soft)}

  .early-bird{position:absolute;left:600px;top:848px;width:260px;text-align:center}
  .early-bird .when{font:400 37px "Arimo",sans-serif;color:var(--ink)}
  .early-bird .deadline{font:400 26px "Arimo",sans-serif;color:var(--ink);margin-top:4px;white-space:nowrap}
  .early-bird .save{font:400 44px "Arimo",sans-serif;color:var(--orange);margin-top:6px}

  .footer-band{position:absolute;left:349px;top:1023px;width:524px;height:107px;background:rgba(13,42,92,.78)}
  .footer-band .url{position:absolute;left:14px;top:12px;font:400 31px "Arimo",sans-serif;color:var(--white);white-space:nowrap}
  .footer-band .phone{position:absolute;left:72px;top:52px;font:700 48px "Arimo",sans-serif;color:var(--orange);-webkit-text-stroke:1.5px #fff;paint-order:stroke fill;white-space:nowrap}

  .register-ribbon{position:absolute;left:0;top:1030px;width:341px;height:124px}
  .register-ribbon span{position:absolute;left:56px;top:16px;font:400 32px/1.3 "Arimo",sans-serif;color:var(--white);text-align:left}
</style>
</head>
<body>
<main class="cover">
  <div class="hero-photo" role="img" aria-label="Photograph of a smiling young professional woman looking upward while working at a laptop in a bright office"></div>

  <header class="header">
    <div class="date-ribbon">
      <svg width="320" height="76" viewBox="0 0 320 76">
        <polygon points="0,0 320,0 320,76 0,76 22,38" fill="var(--ribbon)"/>
        <polygon points="14,6 320,6 320,70 14,70 32,38" fill="#6d98ea"/>
        <polyline points="26,10 318,10" stroke="#cfe0ff" stroke-width="2" stroke-dasharray="6 5"/>
        <polyline points="26,66 318,66" stroke="#cfe0ff" stroke-width="2" stroke-dasharray="6 5"/>
      </svg>
      <span>June 10-12, 2014</span>
    </div>
    <div class="brand"><span>BWKT</span></div>
    <h1 class="title"><span class="lead">Clearpath</span> <span class="rest">Forum Week</span></h1>
    <p class="tagline">Design Compelling Experiences through Successful UX Strategy</p>
  </header>

  <div class="venue-bar">
    <svg width="56" height="32" viewBox="0 0 56 32">
      <rect x="1" y="1" width="54" height="30" fill="#0b1e3c"/>
      <polyline points="1,1 28,20 55,1" fill="none" stroke="#3aa9ea" stroke-width="2.5"/>
      <path d="M1,31 L22,16 M55,31 L34,16" fill="none" stroke="#3aa9ea" stroke-width="2"/>
    </svg>
    <p>Harborline Club &amp; Hotel San Francisco, CA</p>
  </div>

  <section class="bubble bubble-learn">
    <h3>LearnHow</h3>
    <p>UX-Driven<br>Innovation Can<br>Change Your<br>Business</p>
  </section>
  <section class="bubble bubble-cases">
    <h3>Case Studies</h3>
    <p>from Leading<br>Brands on<br>Executing an<br>Effective<br>UX Strategy</p>
  </section>
  <section class="bubble bubble-team">
    <h3>Build A</h3>
    <p>Successful UX<br>Team that<br>Operates<br>Strategically</p>
  </section>
  <section class="bubble bubble-insights">
    <h3>Insights</h3>
    <p>into UX<br>Research, User<br>Behavior,<br>Usability Testing,<br>Lean UX, and<br>More</p>
  </section>

  <aside class="early-bird">
    <p class="when">Register by</p>
    <p class="deadline">March 7th, 2014 and</p>
    <p class="save">SAVE $400!</p>
  </aside>

  <footer>
    <div class="footer-band">
      <p class="url">www.clearpathforumweek.com</p>
      <p class="phone">888.5550.0142</p>
    </div>
    <div class="register-ribbon">
      <svg width="341" height="124" viewBox="0 0 341 124">
        <polygon points="0,0 341,0 318,62 341,124 0,124" fill="var(--red)"/>
        <polyline points="0,8 330,8" stroke="#ffb3b3" stroke-width="2" stroke-dasharray="6 5"/>
        <polyline points="0,116 330,116" stroke="#ffb3b3" stroke-width="2" stroke-dasharray="6 5"/>
      </svg>
      <span>Register<br>Today!</span>
    </div>
  </footer>
</main>
</body>
</html>
```